Business card design needed for a security services business.

We provide a wide range of security services from guard personnel to electronic systems.

Industry/Entity Type

Security Industry

Contact Information for Business Card

Brent Holloway, Owner Office: 780.555.0148; Cell: 780.555.0193 Email: brent@korvanshieldgroup.example; Address 20417 163 St Edmonton, AB T5X 2K8

Colors
0054AA
0677BA
7BADD7
CADEEF
E8F1F8

Requirements
Nice to have
• On the back of the card I would like to possible list the services I provide: Guards Mobiles Live Video Surveillance Access Intrusion

```html
<!DOCTYPE html>
<html lang="en">
<head>
<meta charset="utf-8">
<title>Korvan Shield Group — Business Card</title>
<link href="https://fonts.googleapis.com/css2?family=Montserrat:wght@400;500;700;800&display=swap" rel="stylesheet">
<style>
  :root {
    --brand-deep: #0054AA;
    --brand-blue: #0677BA;
    --brand-sky: #7BADD7;
    --brand-mist: #CADEEF;
    --brand-ice: #E8F1F8;
    --ink-grey: #5a5a5a;
    --paper: #ffffff;
    --backdrop: #2b2d30;
  }
  * { box-sizing: border-box; margin: 0; padding: 0; }
  html, body { width: 1200px; height: 900px; overflow: hidden; }
  body {
    background: var(--backdrop);
    font-family: "Montserrat", Arial, sans-serif;
    position: relative;
  }
  .card {
    position: absolute;
    left: 267px;
    width: 666px;
    height: 380px;
    border-radius: 26px;
    overflow: hidden;
  }
  .card-back { top: 50px; background: var(--brand-blue); color: var(--paper); }
  .card-front { top: 470px; background: var(--paper); color: var(--ink-grey); }

  .wordmark {
    position: absolute;
    left: 0; right: 0;
    text-align: center;
    font-weight: 800;
    text-transform: uppercase;
    letter-spacing: 2px;
    line-height: 1.05;
  }
  .card-back .wordmark { top: 96px; font-size: 46px; color: var(--paper); }
  .card-front .wordmark { top: 52px; font-size: 40px; color: var(--brand-blue); }
  .wordmark .line-sub { display: block; font-size: 0.55em; letter-spacing: 12px; }

  .services {
    position: absolute;
    bottom: 54px; left: 0; right: 0;
    display: flex;
    justify-content: center;
    gap: 28px;
    font-size: 17px;
    font-weight: 500;
  }
  .services li { list-style: none; }
  .services li::before { content: "•"; margin-right: 6px; }

  .name-rule {
    position: absolute;
    top: 222px; left: 42px; right: 42px;
    height: 1.5px;
    background: var(--brand-blue);
  }
  .person {
    position: absolute;
    top: 200px; left: 50%;
    transform: translateX(-50%);
    background: var(--paper);
    padding: 0 18px;
    text-align: center;
  }
  .person-name { font-size: 26px; font-weight: 800; color: var(--brand-blue); text-transform: uppercase; letter-spacing: 0.5px; }
  .person-role { font-size: 16px; font-weight: 500; color: var(--ink-grey); }

  .contact-row {
    position: absolute;
    bottom: 42px; left: 36px; right: 30px;
    display: flex;
    align-items: center;
    font-size: 14.5px;
    color: var(--ink-grey);
  }
  .contact-group { display: flex; flex-direction: column; gap: 8px; }
  .contact-item { display: flex; align-items: center; gap: 7px; white-space: nowrap; }
  .contact-item svg { width: 14px; height: 14px; fill: var(--brand-blue); flex: none; }
  .divider { width: 1.5px; height: 46px; background: var(--brand-blue); margin: 0 18px; flex: none; }
  .address { line-height: 1.45; }
</style>
</head>
<body>

  <section class="card card-back">
    <div class="wordmark">Korvan Shield<span class="line-sub">Group</span></div>
    <ul class="services">
      <li>Guards Mobiles Live</li>
      <li>Video Surveillance</li>
      <li>Access Intrusion</li>
    </ul>
  </section>

  <section class="card card-front">
    <div class="wordmark">Korvan Shield<span class="line-sub">Group</span></div>
    <div class="name-rule"></div>
    <div class="person">
      <div class="person-name">Brent Holloway</div>
      <div class="person-role">Owner</div>
    </div>

    <div class="contact-row">
      <div class="contact-group">
        <div class="contact-item">
          <svg viewBox="0 0 24 24"><path d="M6.6 10.8a15 15 0 0 0 6.6 6.6l2.2-2.2a1 1 0 0 1 1-.25 11.4 11.4 0 0 0 3.6.57 1 1 0 0 1 1 1V20a1 1 0 0 1-1 1A17 17 0 0 1 3 4a1 1 0 0 1 1-1h3.5a1 1 0 0 1 1 1c0 1.25.2 2.45.57 3.57a1 1 0 0 1-.25 1z"/></svg>
          780.555.0148
        </div>
        <div class="contact-item">
          <svg viewBox="0 0 24 24"><path d="M7 1h10a2 2 0 0 1 2 2v18a2 2 0 0 1-2 2H7a2 2 0 0 1-2-2V3a2 2 0 0 1 2-2zm0 3v14h10V4zm5 15.5a1 1 0 1 0 0 2 1 1 0 0 0 0-2z"/></svg>
          780.555.0193
        </div>
      </div>
      <div class="divider"></div>
      <div class="contact-group">
        <div class="contact-item">
          <svg viewBox="0 0 24 24"><path d="M2 5h20v14H2zm2 2v.5l8 5 8-5V7zm0 2.8V17h16V9.8l-8 5z"/></svg>
          brent@korvanshieldgroup.example
        </div>
        <div class="contact-item">
          <svg viewBox="0 0 24 24"><path d="M12 2a10 10 0 1 0 0 20 10 10 0 0 0 0-20zm6.9 6h-3a15 15 0 0 0-1.3-3.9A8 8 0 0 1 18.9 8zM12 4c.9 1.2 1.6 2.6 2 4h-4c.4-1.4 1.1-2.8 2-4zM4.3 14a8 8 0 0 1 0-4h3.4a16 16 0 0 0 0 4zm.8 2h3a15 15 0 0 0 1.3 3.9A8 8 0 0 1 5.1 16zm3-8h-3a8 8 0 0 1 4.3-3.9A15 15 0 0 0 8.1 8zM12 20c-.9-1.2-1.6-2.6-2-4h4c-.4 1.4-1.1 2.8-2 4zm2.3-6H9.7a14 14 0 0 1 0-4h4.6a14 14 0 0 1 0 4zm.3 5.9a15 15 0 0 0 1.3-3.9h3a8 8 0 0 1-4.3 3.9zm1.7-5.9a16 16 0 0 0 0-4h3.4a8 8 0 0 1 0 4z"/></svg>
          www.korvanshieldgroup.example
        </div>
      </div>
      <div class="divider"></div>
      <div class="address">20417 163 St Edmonton,<br>AB T5X 2K8</div>
    </div>
  </section>

</body>
</html>
```